A boutique/architectural website for a landscape company

I'm after a minimilstic boutique website for my landscape design and construction business. I have been exploring Wix and created some pages on that but want something more aesthetic.

Industry/Entity Type

Landscaping design and construction

Number of Pages Required

5+ page

Font styles to use
Sans Serif

Colors

Designer to choose colors to be used in the design.

Requirements
Must have
• an architectural, minimalistic look
Nice to have
• Simplicitly and nice images
Should not have
• A corporate look

```html
<!DOCTYPE html>
<html lang="en">
<head>
<meta charset="utf-8">
<title>Linden – About Us</title>
<link href="https://fonts.googleapis.com/css2?family=Poppins:wght@400;500;600;700&family=Roboto:wght@400;500&family=Noto+Serif:wght@700&display=swap" rel="stylesheet">
<style>
:root{
  --cream:#fefcef;
  --forest:#044a42;
  --sun:#fdc800;
  --name:#f4c21a;
  --ink:#0d0d0d;
  --night:#141214;
  --muted:#6f6b62;
  --white:#ffffff;
}
*{box-sizing:border-box;margin:0;padding:0}
html,body{width:1200px;height:2229px;overflow:hidden}
body{background:var(--cream);color:var(--ink);font-family:"Poppins",sans-serif;position:relative}
.abs{position:absolute}

/* header */
.brand{left:120px;top:0;width:120px;height:110px;background:var(--forest);color:var(--white);display:flex;align-items:center;justify-content:center;font-family:"Poppins",sans-serif;font-weight:600;font-size:17px;letter-spacing:2px}
.main-nav{left:324px;top:31px;display:flex;gap:0;font-family:"Roboto",sans-serif;font-size:14px}
.main-nav a{color:var(--ink);text-decoration:none;position:absolute;white-space:nowrap}
.main-nav .current{text-decoration:line-through}
.btn-start{left:926px;top:17px;width:154px;height:43px;background:var(--forest);color:var(--white);font-family:"Roboto",sans-serif;font-size:16px;font-weight:500;display:flex;align-items:center;justify-content:center;letter-spacing:.3px}

/* about */
.page-title{left:0;width:1200px;top:200px;text-align:center;font-size:33px;font-weight:700;letter-spacing:2px}
.title-rule{left:572px;top:254px;width:62px;height:3px;background:var(--ink)}
.intro{left:368px;top:309px;width:470px;font-size:14.5px;line-height:22px;color:#222}
.solutions{left:288px;top:475px;font-size:24px;font-weight:700;letter-spacing:1.6px;line-height:40px}
.solutions span{position:relative;display:block;z-index:1}
.bar{background:var(--sun);height:10px;z-index:0}
.solutions-text{left:625px;top:476px;width:340px;font-size:14.5px;line-height:22.3px;color:#222}

/* designers */
.section-title{left:0;width:1200px;top:727px;text-align:center;font-size:34px;font-weight:700;letter-spacing:2px}
.designer{top:850px;width:223px}
.designer .photo{width:223px;height:309px}
.designer .name{margin-top:22px;text-align:center;color:var(--name);font-weight:600;font-size:16.5px}
.designer .rule{width:82px;height:1.5px;background:var(--ink);margin:8px auto 0}
.designer .role{margin-top:14px;text-align:center;font-family:"Roboto",sans-serif;font-weight:500;font-size:14px}
.designer .bio{margin-top:24px;font-family:"Roboto",sans-serif;font-size:13.5px;line-height:18.2px;color:#222}

/* banner */
.banner{left:0;top:1436px;width:1200px;height:282px;background:linear-gradient(90deg,#e6d8c8 0%,#efe7da 30%,#e9e4d7 55%,#e4dccd 80%,#ece6da 100%)}
.banner-title{left:0;width:1200px;top:1494px;text-align:center;font-family:"Noto Serif",serif;font-weight:700;font-size:28.5px;line-height:39px;color:#1a1a1a}
.btn-dark{left:471px;top:1613px;width:257px;height:46px;background:var(--night);color:var(--white);font-family:"Roboto",sans-serif;font-size:16px;display:flex;align-items:center;justify-content:center;gap:22px;letter-spacing:.3px}

/* ask */
.ask{left:0;width:1200px;top:1784px;text-align:center;font-weight:600;font-size:21px;letter-spacing:.6px}
.btn-sun{left:514px;top:1848px;width:172px;height:47px;background:var(--sun);color:#1f2a1a;font-size:14px;font-weight:500;letter-spacing:2px;display:flex;align-items:center;justify-content:center}

/* footer */
.footer{left:0;top:1960px;width:1200px;height:269px;background:var(--night);color:var(--white)}
.contact-line{top:66px;font-weight:600;font-size:15.5px;letter-spacing:.5px;white-space:nowrap}
.foot-nav a{position:absolute;top:143px;color:var(--white);text-decoration:none;font-family:"Roboto",sans-serif;font-weight:500;font-size:14.5px;white-space:nowrap}
.foot-rule{top:151px;width:48px;height:1px;background:#9a9a9a}
.social{top:139px;width:22px;height:22px;border:2px solid var(--white);border-radius:50%}
.copyright{left:0;width:1200px;top:2199px;text-align:center;font-size:14px;color:#5b5850}
</style>
</head>
<body>

<header>
  <div class="abs brand">LINDEN</div>
  <nav class="abs main-nav">
    <a style="left:0">HOME</a>
    <a style="left:70px">HOW IT WORKS</a>
    <a style="left:201px">PACKAGES</a>
    <a style="left:302px">PORTOFOLIO</a>
    <a style="left:416px" class="current">ABOUT US</a>
    <a style="left:514px">CONTACT</a>
  </nav>
  <div class="abs btn-start">Start Project</div>
</header>

<main>
  <h1 class="abs page-title">ABOUT US</h1>
  <div class="abs title-rule"></div>
  <p class="abs intro">Lorem ipsum dolor sit amet, consetetur sadipscing elitr, sed diam nonumy eirmod tempor invidunt ut labore et dolore magna aliquyam erat, sed diam voluptua. At vero eos et</p>

  <div class="abs bar" style="left:300px;top:498px;width:232px"></div>
  <div class="abs bar" style="left:309px;top:538px;width:265px"></div>
  <h2 class="abs solutions"><span>OUR SOLUTIONS</span><span>TO YOUR PROBLEMS</span></h2>
  <p class="abs solutions-text">Lorem ipsum dolor sit amet, consetetur sadipscing elitr, sed diam nonumy eirmod tempor invidunt ut labore et dolore magna aliquyam erat, sed diam voluptua. At vero eos et accusam et justo duo dolores et ea</p>

  <h2 class="abs section-title">MEET THE DESIGNERS</h2>

  <article class="abs designer" style="left:241px">
    <div class="photo" role="img" aria-label="Portrait photo of designer John Doe" style="background:linear-gradient(160deg,#c9c9cc,#9d9a98 60%,#d8d6d4)"></div>
    <div class="name">John Doe</div><div class="rule"></div>
    <div class="role">Occupation</div>
    <p class="bio">Lorem ipsum dolor sit amet, consetetur sadipscing elitr, sed diam nonumy eirmod tempor invidunt ut labore et dolore</p>
  </article>
  <article class="abs designer" style="left:489px">
    <div class="photo" role="img" aria-label="Portrait photo of designer Mara Ellison" style="background:linear-gradient(160deg,#e0c33a,#c9a247 55%,#e8c9a8)"></div>
    <div class="name" style="margin-top:20px">Mara Ellison</div><div class="rule"></div>
    <div class="role">Occupation</div>
    <p class="bio">Lorem ipsum dolor sit amet, consetetur sadipscing elitr, sed diam nonumy eirmod tempor invidunt ut labore et dolore</p>
  </article>
  <article class="abs designer" style="left:737px">
    <div class="photo" role="img" aria-label="Portrait photo of designer Theo Barrett" style="background:linear-gradient(160deg,#8f9296,#b6a08d 50%,#e4e6ea)"></div>
    <div class="name">Theo Barrett</div><div class="rule"></div>
    <div class="role">Occupation</div>
    <p class="bio">Lorem ipsum dolor sit amet, consetetur sadipscing elitr, sed diam nonumy eirmod tempor invidunt ut labore et dolore</p>
  </article>

  <section>
    <div class="abs banner" role="img" aria-label="Faded photo of a brick courtyard garden with potted plants and a tiled table"></div>
    <h2 class="abs banner-title">Our Team of Top Designers Will Design<br>Your Outdoors For You</h2>
    <div class="abs btn-dark">Start Your Project
      <svg width="38" height="12" viewBox="0 0 38 12" aria-hidden="true"><path d="M0 6H36M30 1L36 6L30 11" fill="none" stroke="#fff" stroke-width="1"/></svg>
    </div>
  </section>

  <h2 class="abs ask">If You Have Any Questions Feel Free To Ask</h2>
  <div class="abs btn-sun">CONTACT US</div>
</main>

<footer class="abs footer">
  <div class="abs contact-line" style="left:342px">Email :&nbsp;&nbsp;&nbsp; hello@lindenyards.com</div>
  <div class="abs contact-line" style="left:650px">Phone :&nbsp;&nbsp; + 61 300 555 0142</div>
  <nav class="foot-nav">
    <a style="left:120px">HOME</a>
    <a style="left:198px">HOW IT WORKS</a>
    <a style="left:343px">PACKAGES</a>
    <a style="left:777px">PORTOFOLIO</a>
    <a style="left:907px">ABOUT US</a>
    <a style="left:1017px">CONTACT</a>
  </nav>
  <div class="abs foot-rule" style="left:454px"></div>
  <div class="abs social" style="left:527px" aria-label="Social link"></div>
  <div class="abs social" style="left:590px" aria-label="Social link"></div>
  <div class="abs social" style="left:649px" aria-label="Social link"></div>
  <div class="abs foot-rule" style="left:702px"></div>
</footer>
<div class="abs copyright">LINDEN - Landscaping &amp; Design. 2021 © All Rights Reserved</div>

</body>
</html>
```